Letterhead for a busy but slightly unconventional doctor

I need a letterhead for a busy and senior London based medical doctor who specialises in psychiatry.
Letterhead needs to say
Dr Lena Morwen Ostrow MA PhD MRCP MRCPsych
BPR number 3819057
17, Calloway Street
London N4K 2TB
Telephone: 07812 430276
Email: lena.m.ostrow@dovrel.ac.uk
Letterhead needs to be greyscale or black and white. I would like a classic but contemporary look but a bit quirky/unusual.
I will print on pale grey paper so needs to look good with that.
Something a little bit unconventional.
other doctors and patients
Doctor

```html
<!DOCTYPE html>
<html lang="en">
<head>
<meta charset="utf-8">
<title>Dr Lena Morwen Ostrow — Letterhead</title>
<link rel="stylesheet" href="https://fonts.googleapis.com/css2?family=Playfair+Display:wght@700&family=Tinos:ital,wght@1,700&display=swap">
<style>
  :root {
    --paper: #ffffff;
    --ink: #0d0d0d;
    --band: #0a0a0a;
    --band-text: #f4f4f4;
  }
  * { margin: 0; padding: 0; box-sizing: border-box; }
  html, body {
    width: 849px;
    height: 1200px;
    overflow: hidden;
    background: var(--paper);
  }
  .letterhead {
    position: relative;
    width: 849px;
    height: 1200px;
    background: var(--paper);
    color: var(--ink);
  }
  .masthead {
    position: absolute;
    top: 70px;
    left: 0;
    width: 100%;
    text-align: center;
  }
  .mark-dot {
    display: block;
    width: 120px;
    height: 120px;
    margin: 0 auto;
    border-radius: 50%;
    background: var(--ink);
  }
  .name-given {
    margin-top: 62px;
    font-family: "Playfair Display", serif;
    font-weight: 700;
    font-size: 25px;
    letter-spacing: 0.5px;
    line-height: 1;
    text-transform: uppercase;
  }
  .name-family {
    margin-top: 4px;
    font-family: "Playfair Display", serif;
    font-weight: 700;
    font-size: 40px;
    letter-spacing: 1px;
    line-height: 1;
    text-transform: uppercase;
  }
  .footer-band {
    position: absolute;
    left: 0;
    top: 1084px;
    width: 100%;
    height: 90px;
    background: var(--band);
    color: var(--band-text);
    font-family: "Tinos", serif;
    font-style: italic;
    font-weight: 700;
    text-align: center;
  }
  .credentials {
    padding-top: 22px;
    font-size: 18px;
    word-spacing: 2px;
  }
  .credentials .registration { margin-left: 28px; }
  .contact {
    margin-top: 12px;
    font-size: 16px;
    white-space: nowrap;
  }
</style>
</head>
<body>
  <div class="letterhead">
    <header class="masthead">
      <span class="mark-dot" aria-hidden="true"></span>
      <div class="name-given">Dr Lena Morwen</div>
      <div class="name-family">Ostrow</div>
    </header>

    <footer class="footer-band">
      <p class="credentials">MA PhD MRCP MRCPsych<span class="registration">BPR number 3819057</span></p>
      <p class="contact">17, Calloway Street, London N4K 2TB. Telephone: 07812 430276. &nbsp;Email: lena.m.ostrow@dovrel.ac.uk</p>
    </footer>
  </div>
</body>
</html>
```